K.R.V ( the tide beyond morning)CD Cover Design Project

I need a CD eco case designed.
It is a 4 part case with no booklet, plus the CD (matching theme).
My artist name is : K.R.V
The Title of the CD is :(The tide beyond morning)

The music I perform is a collaboration of Hip hop and acoustic music.
My theme is SURFING , NATURE , BEACH DOLPHINS,
SUNRISE,SUNSET ...etc

I would like designs that help people feel the mood of the music before they even put the CD in the player.

Hey all. I really hope you can help me get this done!!

Hey everyone I am on a deadline to get this done so I just upped the budget by $60.

Cant wait to see what people have done!!
Thanks !
Orin.

Target Market(s)

Surfers, hip hop fans, anybody who appreciates music

Requirements
Must have
• I would like the front and back (outside) of the case to be connected (eg using the picture stretched across the two) or have them look very similar at least.
The back outside must have the track names and my website
www.krvsound.net
The inside must have some of my chosen pictures Track details and thanks, that I attached on the PDF file, also the check out these brands/artists stuff. (its ok for the font to be small)
Nice to have
• It would be nice for the outside to be a beach sunset or sunrise, with maybe footprints in the sand and my picture in the sky somwhere. (just an idea, ) please do what feels right and creative for you.
Should not have
• I don't want to see t typical hip hop design.
no guns, no ghetto streets.

```html
<!DOCTYPE html>
<html lang="en">
<head>
<meta charset="utf-8">
<title>K.R.V – The tide beyond morning – inside tray</title>
<link href="https://fonts.googleapis.com/css2?family=Comfortaa:wght@700&display=swap" rel="stylesheet">
<style>
  :root {
    --page: #ffffff;
    --sky: #b9dce6;
    --palm-dark: #3f5a2e;
    --palm-mid: #6f8a43;
    --sand: #e9dcb4;
    --sand-light: #f2e8c8;
    --sea: #7fb7b3;
    --ink: #ffffff;
    --shadow: rgba(20, 25, 10, 0.85);
  }
  * { margin: 0; padding: 0; box-sizing: border-box; }
  html, body { width: 1200px; height: 573px; overflow: hidden; background: var(--page); }
  .spread { position: relative; width: 1200px; height: 573px; font-family: "Comfortaa", sans-serif; font-weight: 700; color: var(--ink); }

  .panel-left {
    position: absolute; left: 35px; top: 35px; width: 565px; height: 513px;
    background:
      linear-gradient(180deg, var(--sky) 0%, #c7dfcf 12%, var(--palm-mid) 26%, var(--palm-dark) 42%, transparent 52%),
      linear-gradient(100deg, var(--sea) 0%, #a8cbb8 28%, var(--sand) 45%, var(--sand-light) 100%);
  }
  .panel-right { position: absolute; left: 620px; top: 35px; width: 545px; height: 513px; }
  .panel-right svg { display: block; }

  .copy { position: absolute; text-shadow: 1px 1px 1px var(--shadow), 0 0 3px var(--shadow), 0 0 0.5px var(--ink); white-space: nowrap; }

  .track { font-size: 12.5px; line-height: 13.6px; }
  .track p { margin: 0; }

  .brands, .artists { font-size: 12.5px; text-align: center; }
  .brands p, .artists p { height: 24.8px; }
  .brands { left: 640px; top: 70px; width: 285px; }
  .artists { left: 925px; top: 116px; width: 225px; }

  .thanks-title { left: 820px; top: 361px; width: 145px; text-align: center; font-size: 12.5px; }
  .thanks-body {
    left: 650px; top: 381px; width: 505px; white-space: normal;
    font-size: 6.6px; line-height: 8.3px;
    text-shadow: 0.5px 0.5px 1px var(--shadow), 0 0 2px var(--shadow);
  }
</style>
</head>
<body>
<main class="spread">
  <section class="panel-left" role="img" aria-label="Tropical beach photograph with palm trees, calm turquoise water and white sand"></section>

  <section class="panel-right">
    <svg width="545" height="513" viewBox="0 0 545 513" role="img" aria-label="Beach photograph with leaning palm trees and green shrubs over pale sand">
      <defs>
        <linearGradient id="palmsSand" x1="0" y1="0" x2="0" y2="1">
          <stop offset="0" stop-color="#b8d8d6"/>
          <stop offset="0.12" stop-color="#7d9650"/>
          <stop offset="0.45" stop-color="#4a6432"/>
          <stop offset="0.62" stop-color="#7a8a4a"/>
          <stop offset="0.75" stop-color="#d9cfa6"/>
          <stop offset="1" stop-color="#e8dcb6"/>
        </linearGradient>
      </defs>
      <path fill="url(#palmsSand)" d="M0 0 H545 V513 H0 V318 Q0 300 18 296 Q32 292 32 276 V150 Q32 134 18 130 Q0 126 0 108 Z"/>
    </svg>
  </section>

  <div class="copy track" style="left:66px; top:57px;">
    <p>海風</p>
    <p>Track performed by K.R.V</p>
    <p>Lyrics by K.R.V</p>
    <p>Beat by TK BEATS</p>
    <p>Recorded @ B-STUDIO</p>
    <p>Recorded by TAVO</p>
    <p>Mix / Mastered by JONAH VERRICK</p>
  </div>

  <div class="copy track" style="left:66px; top:206px;">
    <p>JAPANESE GIRL</p>
    <p>Track performed by K.R.V</p>
    <p>Lyrics by K.R.V</p>
    <p>Beat by GOLDEN REEL BEATS</p>
    <p>Recorded @ B-STUDIO</p>
    <p>Recorded by TAVO</p>
    <p>Mix Mastered by JONAH VERRICK</p>
  </div>

  <div class="copy track" style="left:66px; top:355px;">
    <p>NEVER</p>
    <p>Track performed by K.R.V</p>
    <p>Lyrics by K.R.V</p>
    <p>Beat by MARLOW BEATS</p>
    <p>Recorded @ B-STUDIO</p>
    <p>Recorded by TAVO</p>
    <p>Mix / Mastered by JONAH VERRICK</p>
  </div>

  <div class="copy track" style="left:338px; top:95px;">
    <p>NOWHERE TO RUN</p>
    <p>Track performed by K.R.V / LUMAE</p>
    <p>Lyrics written by V1 &amp; V3 ,K.R.V /</p>
    <p>V2 LUMAE</p>
    <p>Beat by KESTREL BEATS</p>
    <p>Recorded @ B-STUDIO</p>
    <p>Recorded by TAVO</p>
    <p>Mix / Mastered by JONAH VERRICK</p>
  </div>

  <div class="copy track" style="left:338px; top:259px;">
    <p>LONELY WORLD</p>
    <p>Track performed by K.R.V /</p>
    <p>MAPLE ROSE</p>
    <p>Lyrics by K.R.V / MAPLE ROSE</p>
    <p>Beat by JONAH VERRICK</p>
    <p>Recorded @ B-STUDIO</p>
    <p>Recorded by TAVO</p>
    <p>Mix / Mastered by JONAH VERRICK</p>
  </div>

  <div class="copy track" style="left:338px; top:424px;">
    <p>WE ALL STAND UP</p>
    <p>Track performed by K.R.V / TAVO</p>
    <p>Lyrics by K.R.V</p>
    <p>Beat by TAVO</p>
    <p>Recorded @ B-STUDIO</p>
    <p>Recorded by TAVO</p>
    <p>Mix / Mastered by JONAH VERRICK</p>
  </div>

  <div class="copy brands">
    <p>PLEASE CHECK OUT THESE BRANDS</p>
    <p>GLASSWAVE SURFBOARDS</p>
    <p>ECHO APPAREL</p>
    <p>PALM SWELL (surf tours)</p>
    <p>B-STUDIO</p>
    <p>WWW.NK-VENTURES.NET</p>
  </div>

  <div class="copy artists">
    <p>CHECK OUT THESE ARTISTS</p>
    <p>HARE &amp; HOUND</p>
    <p>LUMAE</p>
    <p>MAPLE ROSE</p>
    <p>TAVO</p>
    <p>KUMO SOUND</p>
    <p>THE BLOCK TONE CREW...</p>
    <p>THE 7 XL CREW</p>
    <p>NAGARE</p>
  </div>

  <h2 class="copy thanks-title">THANK YOU</h2>
  <div class="copy thanks-body">
    I would like to say thank you to all my friends and family who kept pushing me to never give up on myself.<br>
    Mia &amp; Kenji you two are my reason for never quitting even when times got rough and I wanted to just pack it in and walk away.<br>
    Mum, thanks for being my inspiration in life, teaching me to help people and to always look for the best inside of someone.<br>
    Hoshino &amp; Tanaka family, thanks for putting up with my noise and accepting me as your family!<br>
    Lumae, thanks for giving me a chance and for looking past appearances and seeing my potential within. I'm forever grateful.<br>
    Tavo, thanks for sitting in that chair day after day until late at night recording my stuff, sometimes we butt heads,<br>
    but all people do, it's those that look past the difference that we call friends.<br>
    Maple R, your a machine! thanks for the good times and being my late night partner! Keep doin your thing.<br>
    Pete &amp; Ali @ Palm Swell, thanks for the lifetime of help and support that continues right through to today.<br>
    Aiko Sato @ Glasswave Surfboards.<br>
    Dario, Wes, Leon, Brennan, Teo, Tyler, Casper, Wynn, Hugo, Remy, Milo and everyone else in the crew!!<br>
    There are so so so many more people I want to thank, but I dont have the space and time, so if I know you and we are friends...<br>
    THANK YOU and if you have this CD... THANK YOU!!
  </div>
</main>
</body>
</html>
```